Business card for communications

Need a business card for my consulting business - I work with not for profits, start ups and social enterprises on their media, communications campaigns.

Please see my website for colours, images and fonts www.morvenquillet.example

Morven Quillet
Communications & Campaign strategist
Sydney - Melbourne
M: 0498 317 250
E: morven@morvenquillet.example
S: morvenquillet
W: morvenquillet.example
T: @morvenquillet

(above is info only and can be presented any way e.g. should not have to be M for mobile - it should be an icon)
Updates

Dear designers I have updated the brief and uploaded high res images from my website for you to use. The designs so far with the use of images and icons are much better so far. Thank you I look forward to receiving your revised designs. Morven Quillet

Industry/Entity Type

Communications

Font styles to use
Sans Serif

Requirements
Must have
• Icons for contact details
Images from the website www.morvenquillet.example
Nice to have
• Images - attached

```html
<!DOCTYPE html>
<html lang="en">
<head>
<meta charset="utf-8">
<title>Morven Quillet – Business Card</title>
<link href="https://fonts.googleapis.com/css2?family=Open+Sans:wght@400;600;700&display=swap" rel="stylesheet">
<style>
  :root {
    --page-bg: #2b2a29;
    --card-dark: #1c1f24;
    --card-stripe: #23272d;
    --lime: #d6ea1c;
    --lime-soft: rgba(214, 234, 28, 0.55);
    --ink: #15171a;
    --white: #f2f2f2;
    --grey-light: #b9b9b9;
    --icon-blue: #3a9be0;
    --desk-dark: #3c3c3c;
    --desk-mid: #7d7d7d;
    --desk-light: #d2d2d2;
  }
  * { box-sizing: border-box; margin: 0; padding: 0; }
  html, body { width: 1200px; height: 750px; overflow: hidden; }
  body {
    background: var(--page-bg);
    font-family: "Open Sans", sans-serif;
    position: relative;
  }
  .card {
    position: absolute;
    top: 205px;
    width: 560px;
    height: 340px;
    overflow: hidden;
    background:
      repeating-linear-gradient(90deg, var(--card-dark) 0 3px, var(--card-stripe) 3px 5px),
      var(--card-dark);
    box-shadow: 0 10px 30px rgba(0,0,0,0.5);
  }
  .card--front { left: 26px; }
  .card--back { left: 614px; }

  /* shared */
  .photo-strip {
    position: absolute;
    left: 0; right: 0;
    background:
      radial-gradient(ellipse 60px 26px at 12% 30%, rgba(210,210,210,0.55), transparent),
      radial-gradient(ellipse 70px 24px at 40% 65%, rgba(210,210,210,0.45), transparent),
      radial-gradient(ellipse 60px 22px at 68% 35%, rgba(210,210,210,0.5), transparent),
      radial-gradient(ellipse 55px 26px at 90% 60%, rgba(210,210,210,0.45), transparent),
      linear-gradient(90deg, var(--desk-dark), var(--desk-mid) 25%, var(--desk-dark) 50%, var(--desk-mid) 75%, var(--desk-dark));
  }
  .lime-rule { position: absolute; left: 0; right: 0; background: var(--lime); }
  .ornament {
    position: absolute;
    border-radius: 50%;
    background: radial-gradient(closest-side, rgba(200,200,200,0.10), rgba(200,200,200,0));
  }

  /* front */
  .name-band {
    position: absolute;
    left: 0; top: 60px;
    width: 545px; height: 58px;
    background: var(--lime);
    box-shadow: 0 4px 8px rgba(0,0,0,0.45);
  }
  .portrait {
    position: absolute;
    left: 54px; top: 32px;
    width: 114px; height: 114px;
    border-radius: 50%;
    border: 6px solid var(--lime);
    background: radial-gradient(circle at 50% 40%, #9b8a80, #4a3f3a 70%);
    box-shadow: 0 4px 10px rgba(0,0,0,0.5);
  }
  .front-name {
    position: absolute;
    left: 208px; top: 64px;
    font-size: 33px; font-weight: 600;
    color: var(--ink);
    line-height: 50px;
  }
  .front-title {
    position: absolute;
    left: 190px; top: 124px;
    font-size: 12.5px; font-weight: 600;
    color: var(--white);
    letter-spacing: 1.4px;
  }
  .card--front .rule-top { top: 210px; height: 3px; }
  .card--front .photo-strip { top: 214px; height: 74px; }
  .card--front .rule-bottom { top: 289px; height: 3px; }
  .signal-line {
    position: absolute;
    height: 2px;
    background: rgba(220,220,220,0.45);
  }

  /* back */
  .back-name {
    position: absolute;
    left: 0; right: 0; top: 50px;
    text-align: center;
    font-size: 33px; font-weight: 600;
    color: var(--lime);
    letter-spacing: 4px;
    line-height: 44px;
    text-shadow: 0 0 8px rgba(214,234,28,0.35), 0 2px 3px rgba(0,0,0,0.8);
  }
  .back-title {
    position: absolute;
    left: 0; right: 0; top: 96px;
    text-align: center;
    font-size: 8.5px; font-weight: 700;
    color: var(--white);
    letter-spacing: 2.6px;
  }
  .thin-rule { position: absolute; height: 1px; background: var(--lime-soft); }
  .back-city {
    position: absolute;
    left: 0; right: 0; top: 116px;
    text-align: center;
    font-size: 12px; font-weight: 600;
    color: var(--white);
    letter-spacing: 1.5px;
  }
  .contacts {
    position: absolute;
    left: 116px; top: 142px;
    display: grid;
    grid-template-columns: 132px 220px;
    row-gap: 18px;
    column-gap: 8px;
  }
  .contact {
    display: flex; align-items: center; gap: 9px;
    font-size: 11px; color: var(--white);
  }
  .contact svg { flex: none; }
  .back-web {
    position: absolute;
    left: 0; right: 0; top: 236px;
    text-align: center;
    font-size: 12px;
    color: var(--grey-light);
    letter-spacing: 6px;
  }
  .card--back .photo-strip { top: 262px; height: 54px; }
</style>
</head>
<body>

  <section class="card card--front">
    <div class="ornament" style="left:340px; top:0; width:220px; height:60px;" role="img" aria-label="Faint decorative bubble pattern"></div>
    <div class="ornament" style="left:40px; top:140px; width:180px; height:66px;" role="img" aria-label="Faint decorative bubble pattern"></div>
    <div class="signal-line" style="left:300px; top:28px; width:120px;"></div>
    <div class="signal-line" style="left:330px; top:36px; width:60px;"></div>

    <div class="name-band"></div>
    <div class="portrait" role="img" aria-label="Portrait photo of Morven Quillet"></div>
    <h1 class="front-name">Morven Quillet</h1>
    <p class="front-title">Communications &amp; Campaign strategist</p>

    <div class="lime-rule rule-top"></div>
    <div class="photo-strip" role="img" aria-label="Black and white photo of a busy office desk from above"></div>
    <div class="lime-rule rule-bottom"></div>
  </section>

  <section class="card card--back">
    <div class="ornament" style="left:0; top:0; width:160px; height:90px;" role="img" aria-label="Faint decorative bubble pattern"></div>
    <div class="ornament" style="left:430px; top:170px; width:130px; height:80px;" role="img" aria-label="Faint decorative bubble pattern"></div>
    <div class="thin-rule" style="left:50px; top:26px; width:260px;"></div>

    <h2 class="back-name">Morven Quillet</h2>
    <p class="back-title">Communications &amp; Campaign strategist</p>
    <div class="thin-rule" style="left:60px; top:112px; width:440px;"></div>
    <p class="back-city">Sydney - Melbourne</p>

    <div class="contacts">
      <div class="contact">
        <svg width="18" height="18" viewBox="0 0 18 18" aria-hidden="true">
          <rect x="1" y="1" width="16" height="16" rx="4" fill="var(--icon-blue)"/>
          <rect x="6" y="3.5" width="6" height="11" rx="1" fill="#fff"/>
          <rect x="7" y="5" width="4" height="7" fill="var(--icon-blue)"/>
        </svg>
        <span>0498 317 250</span>
      </div>
      <div class="contact">
        <svg width="18" height="18" viewBox="0 0 18 18" aria-hidden="true">
          <circle cx="9" cy="9" r="8" fill="var(--icon-blue)"/>
          <rect x="4.5" y="6" width="9" height="6.5" fill="#fff"/>
          <path d="M4.5 6 L9 9.8 L13.5 6" fill="none" stroke="var(--icon-blue)" stroke-width="1"/>
        </svg>
        <span>morven@morvenquillet.example</span>
      </div>
      <div class="contact">
        <svg width="18" height="18" viewBox="0 0 18 18" aria-hidden="true">
          <circle cx="9" cy="9" r="8" fill="var(--icon-blue)"/>
        </svg>
        <span>@morvenquillet</span>
      </div>
      <div class="contact">
        <svg width="18" height="18" viewBox="0 0 18 18" aria-hidden="true">
          <circle cx="9" cy="9" r="8" fill="var(--icon-blue)"/>
        </svg>
        <span>morvenquillet</span>
      </div>
    </div>

    <div class="thin-rule" style="left:60px; top:169px; width:440px;"></div>
    <div class="thin-rule" style="left:60px; top:228px; width:440px;"></div>
    <p class="back-web">morvenquillet.example</p>

    <div class="photo-strip" role="img" aria-label="Black and white photo of laptops and notes on a desk from above"></div>
  </section>

</body>
</html>
```